KTR Associates Business Card

I would like to have a business card designed that uses my current logo and colors. I am not looking for anything to "out there" but can have a little fun so that it stands out.

I have a boutique consulting firm that specializes in strategic planning, change management, leadership development and innovation.

Industry/Entity Type

Leadership

Contact Information for Business Card

Marta Holbeck
President
marta@ktr-associates.example
555-014-2286

```html
<!DOCTYPE html>
<html lang="en">
<head>
<meta charset="utf-8">
<title>KTR Associates Business Card</title>
<link rel="stylesheet" href="https://fonts.googleapis.com/css2?family=Josefin+Sans:wght@400;700&display=swap">
<style>
  :root {
    --bg: #d9d7d2;
    --card-black: #0b0b0b;
    --card-white: #ffffff;
    --ink: #1a1a1a;
    --ink-light: #e8e8e6;
    --green: #2f9a56;
    --green-light: #b9d66a;
    --green-deep: #1f7a3f;
  }
  * { margin: 0; padding: 0; box-sizing: border-box; }
  html, body { width: 1200px; height: 871px; overflow: hidden; }
  body {
    background: var(--bg);
    font-family: "Josefin Sans", sans-serif;
    position: relative;
  }
  .card {
    position: absolute;
    width: 540px;
    height: 308px;
    box-shadow: 0 12px 30px rgba(0,0,0,0.25);
    overflow: hidden;
  }
  .card--front { left: 70px; top: 110px; background: var(--card-black); }
  .card--back { left: 590px; top: 450px; background: var(--card-white); }

  .wordmark {
    position: absolute;
    font-weight: 400;
    letter-spacing: 0.28em;
    text-transform: uppercase;
    white-space: nowrap;
  }
  .card--front .wordmark {
    color: var(--ink-light);
    font-size: 30px;
    left: 0; right: 0; top: 138px;
    text-align: center;
  }
  .card--back .wordmark {
    color: var(--ink);
    font-size: 21px;
    right: 30px; top: 150px;
  }

  .contact { position: absolute; left: 30px; top: 38px; }
  .contact__name {
    font-weight: 700; font-size: 13px; letter-spacing: 0.16em;
    color: var(--ink); text-transform: uppercase;
  }
  .contact__title {
    font-weight: 700; font-size: 8px; letter-spacing: 0.16em;
    color: var(--green); text-transform: uppercase; margin-top: 3px;
  }
  .contact__list { list-style: none; margin-top: 26px; }
  .contact__item {
    display: flex; align-items: center; gap: 14px;
    font-size: 10px; letter-spacing: 0.14em; color: var(--ink);
    height: 17px; text-transform: uppercase;
  }
  .contact__icon { width: 10px; height: 10px; flex: none; }

  .footer-band { position: absolute; left: 0; top: 0; width: 100%; height: 100%; }
  .footer-brush {
    position: absolute; left: 150px; right: 0; top: 196px; height: 34px;
    background: linear-gradient(90deg, var(--green-light), var(--green) 55%, var(--green-deep));
    border-radius: 60% 40% 0 0 / 100% 100% 0 0;
  }
  .footer-url {
    position: absolute; right: 30px; bottom: 22px;
    color: #ffffff; font-size: 11px; letter-spacing: 0.2em;
    font-weight: 700; text-transform: uppercase;
  }
</style>
</head>
<body>
  <section class="card card--front" aria-label="Card front">
    <div class="wordmark">KTR Associates</div>
  </section>

  <section class="card card--back" aria-label="Card back">
    <div class="contact">
      <div class="contact__name">Marta Holbeck</div>
      <div class="contact__title">President</div>
      <ul class="contact__list">
        <li class="contact__item">
          <svg class="contact__icon" viewBox="0 0 10 10"><path d="M2 1 L4 1 L4.6 3.2 L3.4 4 Q4.6 6 6 6.6 L6.8 5.4 L9 6 L9 8 Q5 9 1 5 Q1 3 2 1Z" fill="var(--green)"/></svg>
          555-014-2286
        </li>
        <li class="contact__item">
          <svg class="contact__icon" viewBox="0 0 10 10"><rect x="0.5" y="2" width="9" height="6" fill="none" stroke="var(--green)"/><path d="M0.5 2 L5 5.5 L9.5 2" fill="none" stroke="var(--green)"/></svg>
          marta@ktr-associates.example
        </li>
        <li class="contact__item">
          <svg class="contact__icon" viewBox="0 0 10 10"><circle cx="5" cy="5" r="4.2" fill="none" stroke="var(--green)"/><ellipse cx="5" cy="5" rx="1.8" ry="4.2" fill="none" stroke="var(--green)"/><path d="M0.8 5 H9.2" stroke="var(--green)"/></svg>
          www.ktr-associates.example
        </li>
      </ul>
    </div>

    <div class="wordmark">KTR Associates</div>

    <svg class="footer-band" viewBox="0 0 540 308" preserveAspectRatio="none" aria-hidden="true">
      <path d="M130 228 Q330 200 540 226 L540 308 L0 308 L0 250 Q60 236 130 228Z" fill="var(--card-black)"/>
    </svg>
    <div class="footer-brush" role="img" aria-label="Green brush-stroke texture along the top of the black band"></div>
    <div class="footer-url">www.ktr-associates.example</div>
  </section>
</body>
</html>
```